電子書籍のタイトル

「窓辺に咲いた小さな灯と
心が旅をする十二の物語」

初めての出版になります。

基本デザインはお任せいたします。

デザインされる参考に添付内容の本文をお読みいください。

想定される読者の方の心に届く表紙にしたいと思います。

どうぞよろしくお願いいたします。

デザイン、文字の配置、色合いから総合的本の内容を表現されているように思いました。

この度は、表紙デザインにたくさんの方がご応募頂き誠にありがとうございました。
素晴らしい作品をたくさん頂き、正直悩みましたが、コンペという事で好みで選択させていただきました。本当に感謝申し上げます。

```html
<!DOCTYPE html>
<html lang="ja">
<head>
<meta charset="utf-8">
<title>窓辺に咲いた小さな灯と 心が旅をする十二の物語</title>
<link href="https://fonts.googleapis.com/css2?family=Noto+Sans+JP:wght@500;700;900&family=Noto+Serif+JP:wght@700;900&display=swap" rel="stylesheet">
<style>
  :root{
    --paper:#ffffff;
    --ink:#1a1a1a;
    --accent:#e8303a;
    --sun:#fff200;
    --sun-soft:#fff59a;
    --rule:#555555;
    --night:#2a2a4a;
  }
  *{margin:0;padding:0;box-sizing:border-box}
  html,body{width:750px;height:1200px;overflow:hidden;background:var(--paper)}
  .cover{position:relative;width:750px;height:1200px;background:var(--paper);font-family:"Noto Sans JP",sans-serif;color:var(--ink)}
  .hero-art{position:absolute;left:490px;top:0;width:235px;height:140px;background:linear-gradient(135deg,#fde3ea,#f7b7c6);border-radius:0 0 60px 60px}
  .title{position:absolute;left:40px;top:60px;font-weight:900;line-height:1}
  .title .lead{display:block;font-size:50px;font-weight:700}
  .title .main{display:block;font-size:74px;margin-top:28px;letter-spacing:1px}
  .title .key{display:block;font-size:76px;margin-top:44px;letter-spacing:2px}
  .title .key em{font-style:normal;color:var(--accent);background:linear-gradient(transparent 62%,var(--sun-soft) 62%)}
  .rule{position:absolute;left:40px;width:670px;height:7px;border-top:2px solid var(--rule);border-bottom:2px solid var(--rule)}
  .rule.top{top:372px}
  .rule.bottom{top:510px}
  .subtitle{position:absolute;left:40px;top:402px;font-size:88px;font-weight:900;line-height:1;letter-spacing:3px}
  .author{position:absolute;left:40px;top:574px;font-size:26px;font-weight:500}
  .band{position:absolute;left:0;top:615px;width:750px;height:585px;background:var(--sun)}
  .moon-art{position:absolute;left:60px;top:630px;width:290px;height:220px;background:radial-gradient(circle at 45% 45%,#fffbd0,var(--sun) 70%);border-radius:50%}
  .gift{position:absolute;left:28px;top:900px;width:320px;height:262px;background:var(--paper);border:3px solid var(--ink);border-radius:26px;padding:22px 10px;text-align:center;font-family:"Noto Serif JP",serif;font-weight:900;font-size:28px;line-height:1.38}
  .gift .gift-head{color:var(--accent);margin-bottom:4px}
  .motto{position:absolute;top:632px;writing-mode:vertical-rl;font-family:"Noto Serif JP",serif;font-weight:900;font-size:74px;line-height:1;color:var(--accent);letter-spacing:2px}
  .motto.c1{left:625px}
  .motto.c2{left:505px}
  .motto.c3{left:388px}
  .motto .big{color:var(--paper);font-size:96px;-webkit-text-stroke:2px var(--accent)}
</style>
</head>
<body>
<main class="cover">
  <div class="hero-art" role="img" aria-label="ハートを抱えて歩く人物のイラスト"></div>

  <h1 class="title">
    <span class="lead">窓辺に咲いた</span>
    <span class="main">小さな灯と</span>
    <span class="key"><em>心が旅</em>をする</span>
  </h1>

  <div class="rule top"></div>
  <p class="subtitle">十二の物語</p>
  <div class="rule bottom"></div>

  <p class="author">真理探究メンタルコーチ Harune 著</p>

  <section class="band">
  </section>
  <div class="moon-art" role="img" aria-label="三日月と星、海の線画イラスト"></div>

  <aside class="gift">
    <p class="gift-head">読者プレゼント</p>
    <p>人生をリセット</p>
    <p>再構築するための</p>
    <p>マインドセット</p>
    <p>7つのシークレット</p>
    <p>メッセージ</p>
  </aside>

  <p class="motto c1">人生は自分と</p>
  <p class="motto c2">出会い続ける</p>
  <p class="motto c3"><span class="big">旅</span>である</p>
</main>
</body>
</html>
```